5 facebook (and instagram) posts for advertising a service of Online Medicine.
This is NOT a facebook page design. This is just facebook (and Instagram) posts design.

We are a medical company providing medicine at distance, using standard videoconsultation and sometimes videoconsultation with a medical device that collects vital signs.

Each post should have:
- Our logo (attached) – if needed it can be just the circular form, but that´s up to you to decide. Ofcourse some design work can be done to this form (watermark, change in dimension, etc)
- Some posts can have the photo of the device (not all the posts because we also provide videoconsultations without the device) – for this please use our website to collect images (https://www.casaorvalhoverde.com/en/kordalix). You can also use the video of the device to collect images (provided as attachment).
- Some stock image at your decision or collected from our website (https://www.casaorvalhoverde.com/pt/medicina-online) or from the provided video (all of these are licensed and you can use them freely – for instance you can collect doctors from our video)
- One or more of the following headlines (please use different headlines for different posts):
 Revolução na Qualidade da Videoconsulta
 O seu Médico com acesso à informação da sua Orrin Wellbook
 Sincronização com Orrin Wellbook
 Possibilidade de usar o dispositivo Kordalix | Medição à Distância de 6 Sinais Vitais
 Revolução na Saúde
 Revolução na Medicina à Distância
 Um Novo Mundo na Saúde
 Segurança e Fiabilidade na Medicina à Distância
 Excelência na Medicina à Distância
 Baixa Médica Online
 Atestados de Saúde
 Renovação de Receituário
 Planos de Monitorização Remota e Acompanhamento Médico desde 10 EUR / Mês

We need 5 posts, all different between each other but where we can feel an aesthetical and graphic/design continuity/coherence of course.
Each post should be provided on adequate format for facebook and Instagram publishing.

Target Market(s)

Patients

Industry/Entity Type

Medicine

Requirements
Must have
• Check description
Nice to have
• Check description

```html
<!DOCTYPE html>
<html lang="pt">
<head>
<meta charset="utf-8">
<title>Casa Orvalho Verde – Videoconsulta</title>
<link href="https://fonts.googleapis.com/css2?family=Barlow+Semi+Condensed:wght@500;600;700&family=Poppins:wght@300;400;500&display=swap" rel="stylesheet">
<style>
  :root{
    --bg:#deebfb;
    --ink:#0f1b2a;
    --brand:#22a5d6;
    --card:#eef5fd;
    --badge-ink:#2c3450;
    --tile-grey:#d9dbe0;
    --tile-blue:#a9c6da;
    --tile-lilac:#d7d8e4;
    --dash:#7fbfe4;
    --dash-soft:#c3dcf2;
  }
  *{margin:0;padding:0;box-sizing:border-box}
  html,body{width:1200px;height:1200px;overflow:hidden;background:var(--bg)}
  .post{position:relative;width:1200px;height:1200px;background:var(--bg);font-family:"Poppins",sans-serif;overflow:hidden}

  .brand{position:absolute;left:374px;top:44px;display:flex;align-items:center;gap:18px}
  .brand-dot{width:96px;height:96px;border-radius:50%;background:var(--brand)}
  .brand-name{font-family:"Barlow Semi Condensed",sans-serif;font-weight:700;color:var(--brand);font-size:50px;line-height:46px;text-transform:uppercase;letter-spacing:1px;width:360px}
  .brand-sub{font-family:"Poppins",sans-serif;font-weight:400;color:var(--brand);font-size:19px;margin-top:6px;letter-spacing:.2px}

  .headline{position:absolute;left:0;width:1200px;top:248px;text-align:center;font-family:"Barlow Semi Condensed",sans-serif;font-weight:700;font-size:92px;color:var(--ink);line-height:1}
  .headline .accent{color:var(--brand);position:relative;display:inline-block}
  .accent-line{position:absolute;left:0;bottom:-10px;width:100%;height:12px}
  .subline{position:absolute;left:0;width:1200px;top:353px;text-align:center;font-weight:300;font-size:35px;color:var(--ink)}

  .orbit{position:absolute;left:0;top:0}

  .tile{position:absolute;width:262px;height:262px;border-radius:22px}
  .tile-left{left:300px;top:620px;background:linear-gradient(160deg,var(--tile-grey),#cfd6de);transform:rotate(-32deg)}
  .tile-right{left:650px;top:600px;background:linear-gradient(160deg,var(--tile-lilac),#c9ccd9);transform:rotate(32deg)}
  .tile-center{left:482px;top:549px;background:linear-gradient(180deg,var(--tile-blue),#c3d6e4)}

  .badge{position:absolute;left:131px;top:490px;width:293px;height:129px;background:var(--card);border-radius:26px;box-shadow:0 10px 30px rgba(34,165,214,.12);display:flex;align-items:center;gap:26px;padding-left:30px}
  .badge-icon{width:78px;height:78px;border-radius:50%;background:#d4e6f3;display:flex;align-items:center;justify-content:center}
  .badge-text{font-weight:500;font-size:19px;line-height:25px;color:var(--badge-ink)}

  .chip{position:absolute;width:56px;height:56px;border-radius:50%;background:var(--brand);display:flex;align-items:center;justify-content:center;box-shadow:0 0 0 6px rgba(255,255,255,.55)}

  .cta{position:absolute;left:293px;top:969px;width:614px;height:114px;border-radius:57px;background:var(--brand);color:#fff;font-family:"Barlow Semi Condensed",sans-serif;font-weight:500;font-size:45px;display:flex;align-items:center;justify-content:center;box-shadow:0 12px 28px rgba(34,165,214,.3)}
  .url{position:absolute;left:0;width:1200px;top:1088px;text-align:center;font-weight:400;font-size:33px;color:var(--ink)}
</style>
</head>
<body>
<main class="post">
  <header class="brand">
    <div class="brand-dot"></div>
    <div>
      <div class="brand-name">Casa Orvalho Verde</div>
      <div class="brand-sub">Professor Doutor Rui Tavoleira</div>
    </div>
  </header>

  <h1 class="headline">Revolução na <span class="accent">Saúde<svg class="accent-line" viewBox="0 0 320 12" preserveAspectRatio="none"><path d="M2 8 Q160 2 318 6" stroke="#22a5d6" stroke-width="4" fill="none" stroke-linecap="round"/></svg></span></h1>
  <p class="subline">através de videoconsulta</p>

  <svg class="orbit" width="1200" height="1200" aria-hidden="true">
    <path d="M331 960 A328 328 0 1 1 913 960" fill="none" stroke="var(--dash)" stroke-width="2.5" stroke-dasharray="34 26"/>
    <path d="M398 960 A270 270 0 1 1 846 960" fill="none" stroke="var(--dash-soft)" stroke-width="2" stroke-dasharray="20 22"/>
  </svg>

  <div class="tile tile-left" role="img" aria-label="Fotografia de médica sorridente com estetoscópio"></div>
  <div class="tile tile-right" role="img" aria-label="Fotografia de médico sorridente com estetoscópio"></div>
  <div class="tile tile-center" role="img" aria-label="Fotografia de médica sorridente de bata branca"></div>

  <div class="badge">
    <div class="badge-icon">
      <svg width="40" height="44" viewBox="0 0 40 44"><path d="M20 2 L36 8 V20 C36 31 29 38 20 42 C11 38 4 31 4 20 V8 Z" fill="#22a5d6"/><path d="M13 22 L18 27 L28 16" stroke="#fff" stroke-width="3.5" fill="none" stroke-linecap="round" stroke-linejoin="round"/></svg>
    </div>
    <div class="badge-text">Consulta de<br>Rotina ou<br>Urgência</div>
  </div>

  <div class="chip" style="left:770px;top:503px">
    <svg width="30" height="30" viewBox="0 0 30 30"><path d="M15 26 C6 19 3 14 3 10 A6 6 0 0 1 15 7 A6 6 0 0 1 27 10 C27 14 24 19 15 26Z" fill="none" stroke="#fff" stroke-width="2"/><circle cx="20" cy="20" r="6" fill="#fff"/><path d="M20 17 V20 H22" stroke="#22a5d6" stroke-width="1.6" fill="none"/></svg>
  </div>
  <div class="chip" style="left:263px;top:774px">
    <svg width="28" height="30" viewBox="0 0 28 30"><rect x="4" y="4" width="20" height="24" rx="3" fill="none" stroke="#fff" stroke-width="2"/><rect x="10" y="1" width="8" height="5" rx="1.5" fill="#fff"/><path d="M8 14 H11 L13 10 L15 17 L17 14 H20 M8 21 H20" stroke="#fff" stroke-width="1.8" fill="none"/></svg>
  </div>
  <div class="chip" style="left:892px;top:811px">
    <svg width="24" height="26" viewBox="0 0 24 26"><path d="M6 2 C2 2 1 6 2 10 C3 14 4 24 7 24 C9 24 9 16 12 16 C15 16 15 24 17 24 C20 24 21 14 22 10 C23 6 22 2 18 2 C15 2 14 4 12 4 C10 4 9 2 6 2Z" fill="#fff"/></svg>
  </div>

  <a class="cta">Marque a sua consulta</a>
  <p class="url">casaorvalhoverde.com</p>
</main>
</body>
</html>
```